Simple and clean webdesign for personal homepage

Trying to create a simple and clean webdesign for my personal homepage. Going to use a static site builder with templates to build the site. I want it to have multiple pages - like an about me, blog and resume. I just need something very basic I can customize. I want the main colors to be purple, black and white. I am open to other color palettes too but since purple is my favorite color I want that to be one of the main colors.

The site be mostly text driven. Might have some images in the body text but I want the site design to be light and lean.

Industry/Entity Type

Personal Homepage.

Coding

Coded - Design and coding required

Number of Pages Required

1 page

Font styles to use
Sans Serif

Colors
6B429C
8869AF
B7A5CE
E3DAEB
F3F0F8

Requirements
Must have
• Clean design. Purple used as a color. HTML template.
Nice to have
• Responsive

```html
<!DOCTYPE html>
<html lang="en">
<head>
<meta charset="UTF-8">
<title>Your Name Here — Personal Homepage</title>
<link rel="stylesheet" href="https://fonts.googleapis.com/css2?family=Montserrat:wght@400;500;600;700;800&display=swap">
<style>
  :root{
    --purple-dark:#6B429C;
    --purple:#8869AF;
    --purple-mid:#B7A5CE;
    --purple-light:#E3DAEB;
    --purple-pale:#F3F0F8;
    --about-bg:#E0CDF2;
    --band-bg:#C8B0EA;
    --accent-line:#9B6DDB;
    --tile:#E8DBFA;
    --text:#1c1a20;
    --muted:#8a8592;
    --white:#ffffff;
  }
  *{box-sizing:border-box;margin:0;padding:0}
  html,body{width:1200px;height:4167px;overflow:hidden}
  body{font-family:"Montserrat",sans-serif;background:var(--white);color:var(--text);position:relative}
  .abs{position:absolute}

  /* Hero */
  .hero{left:37px;top:37px;width:1124px;height:599px;
    background:linear-gradient(135deg,#caa3d6 0%,#e4d2e8 30%,#bfd4e0 55%,#d8c2e4 75%,#cfb3da 100%)}
  .hero-welcome{position:absolute;top:126px;left:0;width:100%;text-align:center;padding-left:0;
    color:var(--white);font-size:22px;letter-spacing:16px;font-weight:400;text-indent:16px}
  .hero-name{position:absolute;left:468px;top:243px;width:190px;height:113px;background:var(--white);
    display:flex;align-items:center;justify-content:center;text-align:center;
    color:var(--purple-mid);font-weight:700;font-size:26px;line-height:32px}

  /* Section title */
  .section-title{font-size:32px;font-weight:700;color:var(--purple-dark);line-height:40px}
  .section-title::after{content:"";display:block;width:210px;height:3px;background:var(--accent-line);margin-top:13px}
  .sub-title{font-size:21px;font-weight:500;color:var(--text);line-height:26px}
  .sub-title::after{content:"";display:block;width:210px;height:3px;margin-top:12px;
    background:linear-gradient(to right,var(--purple-dark) 0 68px,var(--purple-mid) 68px)}

  /* About */
  .about{left:0;top:674px;width:1200px;height:498px;background:var(--about-bg)}
  .about .section-title{position:absolute;left:86px;top:89px}
  .about-text{position:absolute;left:86px;top:190px;width:630px;color:var(--purple-dark);font-size:13px;line-height:24.5px}
  .about-text p{margin-bottom:24.5px}
  .about-contact{position:absolute;left:881px;top:216px;color:var(--purple-dark);font-size:12.5px;font-weight:700;list-style:none}
  .about-contact li{height:49px}

  /* Touch band */
  .touch{left:0;top:1172px;width:1200px;height:177px;background:var(--band-bg);text-align:center}
  .touch h2{font-size:32px;font-weight:500;color:var(--purple-dark);margin-top:35px;line-height:40px}
  .touch-btn{display:inline-block;margin-top:24px;width:202px;height:39px;line-height:39px;background:var(--white);
    color:var(--purple-dark);font-size:13px;font-weight:500}

  /* Resume */
  .resume-title{left:86px;top:1500px}
  .col-left{left:86px;width:520px}
  .col-right{left:661px;width:460px}
  .entries{margin-top:34px}
  .entry{margin-bottom:34px;padding-left:0}
  .entry-head{display:flex;align-items:center;gap:31px}
  .year{width:69px;height:25px;border:2px solid var(--purple-mid);font-size:13px;display:flex;align-items:center;justify-content:center}
  .school{color:var(--purple);font-size:13px}
  .entry h4{margin:11px 0 0 50px;font-size:16px;font-weight:600;line-height:22px}
  .entry p{margin:7px 0 0 50px;font-size:13px;line-height:24px;width:440px}

  .tags{display:flex;flex-wrap:wrap;gap:15px 15px;margin-top:26px;width:460px}
  .tag{background:var(--purple-dark);color:var(--white);font-size:13px;height:25px;line-height:25px;padding:0 8px}

  .certs{margin-top:30px;display:flex;flex-direction:column;gap:16px}
  .cert{width:451px;height:133px;border:3px solid var(--purple-mid);display:flex;padding:8px;gap:20px}
  .cert-img{width:154px;height:113px;background:var(--tile)}
  .cert h4{font-size:16px;font-weight:600;margin-top:4px}
  .cert p{font-size:13px;line-height:24px;color:var(--muted);margin-top:4px}
  .cert time{display:block;font-size:13px;color:var(--muted);margin-top:14px}

  /* Blog */
  .blog-title{left:86px;top:2776px}
  .posts{left:139px;top:2889px;width:922px}
  .post{height:235px;border-bottom:2px solid var(--purple-mid);display:flex;gap:53px;padding-left:16px}
  .post-img{width:212px;height:118px;background:linear-gradient(120deg,#a5704f 0%,#d9c9b8 45%,#eae4dc 70%,#8a8f99 100%)}
  .post-body{width:620px}
  .post h3{font-size:21px;font-weight:800;line-height:26px;margin-top:6px}
  .post-meta{display:flex;gap:18px;font-size:13px;margin-top:11px;color:var(--muted);font-weight:500}
  .post-meta .cat{color:var(--purple-dark);font-weight:600}
  .post p{font-size:13px;line-height:24px;margin-top:10px}
  .post-actions{display:flex;align-items:center;font-size:13px;color:var(--muted);margin-top:14px}
  .action{display:flex;align-items:center;gap:8px;margin-right:43px}
  .post-actions time{margin-left:auto;margin-right:130px}
  .load-more{left:0;top:3891px;width:1200px;display:flex;justify-content:center;align-items:center;gap:14px;font-size:13px;color:var(--muted)}

  /* Footer */
  .footer{left:0;top:3999px;width:1200px;height:168px;background:var(--band-bg)}
  .footer-logo{position:absolute;left:86px;top:34px;width:108px;height:65px;background:var(--white);
    display:flex;align-items:center;justify-content:center;text-align:center;color:var(--purple-mid);font-weight:700;font-size:15px;line-height:19px}
  .social{position:absolute;right:86px;top:56px;display:flex;gap:18px;list-style:none}
  .social li{display:flex;align-items:center;gap:5px;color:var(--white);font-size:11px;font-weight:600}
  .social li::before{content:"";width:10px;height:10px;background:var(--white)}
  .copyright{position:absolute;left:0;width:100%;top:128px;text-align:center;color:var(--white);font-size:12px}
</style>
</head>
<body>

<header class="hero abs">
  <div class="hero-welcome">Welcome</div>
  <div class="hero-name">Your Name<br>Here</div>
</header>

<section class="about abs">
  <h2 class="section-title">About Me</h2>
  <div class="about-text">
    <p>Lorem ipsum dolor sit amet, consectetur adipiscing elit. Ut sed orci vitae mattis tincidunt sagittis auctor feugiat et.</p>
    <p>Eu sodales nunc, risus nisl fusce at urna ultrices. Diam a diam in ultrices nulla. Habitasse habitant neque a, turpis diam lacus quisque. Tempor eu ornare interdum dui. Auctor diam nec, id vehicula metus sit lacus. Consectetur cursus viverra porta odio lacus felis quis.</p>
    <p>Aliquet eget sagittis, amet risus. Gravida viverra dictumst cras eget et enim sodales venenatis, faucibus.</p>
  </div>
  <ul class="about-contact">
    <li>Email:mail@lavendermail.com</li>
    <li>Phone:+77 022 555 01 23</li>
    <li>Study:Univercity of Lakeview</li>
  </ul>
</section>

<section class="touch abs">
  <h2>Let’s Get In Touch</h2>
  <a class="touch-btn">Let’s Get In Touch</a>
</section>

<h2 class="section-title resume-title abs">Resume</h2>

<section class="col-left abs" style="top:1600px">
  <h3 class="sub-title">Education</h3>
  <div class="entries">
    <article class="entry"><div class="entry-head"><span class="year">2010</span><span class="school">University of Study</span></div><h4>Lorem Ipsum Dolor</h4><p>Lorem ipsum dolor sit amet, consectetur adipiscing elit. Ut sed orci vitae mattis tincidunt sagittis auctor feugiat et.</p></article>
    <article class="entry"><div class="entry-head"><span class="year">2010</span><span class="school">University of Study</span></div><h4>Lorem Ipsum Dolor</h4><p>Lorem ipsum dolor sit amet, consectetur adipiscing elit. Ut sed orci vitae mattis tincidunt sagittis auctor feugiat et.</p></article>
    <article class="entry"><div class="entry-head"><span class="year">2010</span><span class="school">University of Study</span></div><h4>Lorem Ipsum Dolor</h4><p>Lorem ipsum dolor sit amet, consectetur adipiscing elit. Ut sed orci vitae mattis tincidunt sagittis auctor feugiat et.</p></article>
  </div>
</section>

<section class="col-left abs" style="top:2103px">
  <h3 class="sub-title">Education</h3>
  <div class="entries">
    <article class="entry"><div class="entry-head"><span class="year">2010</span><span class="school">University of Study</span></div><h4>Lorem Ipsum Dolor</h4><p>Lorem ipsum dolor sit amet, consectetur adipiscing elit. Ut sed orci vitae mattis tincidunt sagittis auctor feugiat et.</p></article>
    <article class="entry"><div class="entry-head"><span class="year">2010</span><span class="school">University of Study</span></div><h4>Lorem Ipsum Dolor</h4><p>Lorem ipsum dolor sit amet, consectetur adipiscing elit. Ut sed orci vitae mattis tincidunt sagittis auctor feugiat et.</p></article>
    <article class="entry"><div class="entry-head"><span class="year">2010</span><span class="school">University of Study</span></div><h4>Lorem Ipsum Dolor</h4><p>Lorem ipsum dolor sit amet, consectetur adipiscing elit. Ut sed orci vitae mattis tincidunt sagittis auctor feugiat et.</p></article>
  </div>
</section>

<section class="col-right abs" style="top:1600px">
  <h3 class="sub-title">Skills</h3>
  <div class="tags">
    <span class="tag">Lorem Ipsum Dolor</span><span class="tag">Lorem Ipsum</span><span class="tag">Lorem Ipsum Dolor</span>
    <span class="tag">Lorem Ipsum</span><span class="tag">Lorem Ipsum</span><span class="tag">Lorem Ipsum Dolor</span>
  </div>
</section>

<section class="col-right abs" style="top:1851px">
  <h3 class="sub-title">Knowledges</h3>
  <div class="tags">
    <span class="tag">Lorem Ipsum Dolor</span><span class="tag">Lorem Ipsum</span><span class="tag">Lorem Ipsum Dolor</span>
    <span class="tag">Lorem Ipsum</span><span class="tag">Lorem Ipsum</span><span class="tag">Lorem Ipsum Dolor</span>
  </div>
</section>

<section class="col-right abs" style="top:2103px">
  <h3 class="sub-title">Sertificates</h3>
  <div class="certs">
    <article class="cert"><div class="cert-img" role="img" aria-label="Certificate image"></div><div><h4>Lorem Ipsum Dolor</h4><p>Lorem ipsum dolor sit amet,<br>consectetur adipiscing elit.</p><time>02 March 2009</time></div></article>
    <article class="cert"><div class="cert-img" role="img" aria-label="Certificate image"></div><div><h4>Lorem Ipsum Dolor</h4><p>Lorem ipsum dolor sit amet,<br>consectetur adipiscing elit.</p><time>02 March 2009</time></div></article>
    <article class="cert"><div class="cert-img" role="img" aria-label="Certificate image"></div><div><h4>Lorem Ipsum Dolor</h4><p>Lorem ipsum dolor sit amet,<br>consectetur adipiscing elit.</p><time>02 March 2009</time></div></article>
  </div>
</section>

<h2 class="section-title blog-title abs">Blog</h2>

<section class="posts abs">
  <article class="post">
    <div class="post-img" role="img" aria-label="Photo of two colleagues celebrating at an office desk with a laptop"></div>
    <div class="post-body">
      <h3>Lorem ipsum dolor sit amet, consectetur adipiscing elit</h3>
      <div class="post-meta"><span class="cat">Category</span><span>Sub Category</span><span>By Author</span></div>
      <p>Lorem ipsum dolor sit amet, consectetur adipiscing elit. Ut sed orci vitae mattis tincidunt sagittis auctor feugiat et.</p>
      <div class="post-actions">
        <span class="action"><svg width="18" height="22" viewBox="0 0 18 22" fill="none" stroke="#8a8592" stroke-width="1.4"><path d="M1 1h16v20l-8-6-8 6z"/></svg>Save</span>
        <span class="action"><svg width="22" height="22" viewBox="0 0 22 22" fill="none" stroke="#8a8592" stroke-width="1.4"><circle cx="17" cy="4" r="3"/><circle cx="5" cy="11" r="3"/><circle cx="17" cy="18" r="3"/><path d="M8 9.5l6-4M8 12.5l6 4"/></svg>Share</span>
        <time>March 02, 2009</time>
      </div>
    </div>
  </article>
  <article class="post">
    <div class="post-img" role="img" aria-label="Photo of two colleagues celebrating at an office desk with a laptop"></div>
    <div class="post-body">
      <h3>Lorem ipsum dolor sit amet, consectetur adipiscing elit</h3>
      <div class="post-meta"><span class="cat">Category</span><span>Sub Category</span><span>By Author</span></div>
      <p>Lorem ipsum dolor sit amet, consectetur adipiscing elit. Ut sed orci vitae mattis tincidunt sagittis auctor feugiat et.</p>
      <div class="post-actions">
        <span class="action"><svg width="18" height="22" viewBox="0 0 18 22" fill="none" stroke="#8a8592" stroke-width="1.4"><path d="M1 1h16v20l-8-6-8 6z"/></svg>Save</span>
        <span class="action"><svg width="22" height="22" viewBox="0 0 22 22" fill="none" stroke="#8a8592" stroke-width="1.4"><circle cx="17" cy="4" r="3"/><circle cx="5" cy="11" r="3"/><circle cx="17" cy="18" r="3"/><path d="M8 9.5l6-4M8 12.5l6 4"/></svg>Share</span>
        <time>March 02, 2009</time>
      </div>
    </div>
  </article>
  <article class="post">
    <div class="post-img" role="img" aria-label="Photo of two colleagues celebrating at an office desk with a laptop"></div>
    <div class="post-body">
      <h3>Lorem ipsum dolor sit amet, consectetur adipiscing elit</h3>
      <div class="post-meta"><span class="cat">Category</span><span>Sub Category</span><span>By Author</span></div>
      <p>Lorem ipsum dolor sit amet, consectetur adipiscing elit. Ut sed orci vitae mattis tincidunt sagittis auctor feugiat et.</p>
      <div class="post-actions">
        <span class="action"><svg width="18" height="22" viewBox="0 0 18 22" fill="none" stroke="#8a8592" stroke-width="1.4"><path d="M1 1h16v20l-8-6-8 6z"/></svg>Save</span>
        <span class="action"><svg width="22" height="22" viewBox="0 0 22 22" fill="none" stroke="#8a8592" stroke-width="1.4"><circle cx="17" cy="4" r="3"/><circle cx="5" cy="11" r="3"/><circle cx="17" cy="18" r="3"/><path d="M8 9.5l6-4M8 12.5l6 4"/></svg>Share</span>
        <time>March 02, 2009</time>
      </div>
    </div>
  </article>
  <article class="post">
    <div class="post-img" role="img" aria-label="Photo of two colleagues celebrating at an office desk with a laptop"></div>
    <div class="post-body">
      <h3>Lorem ipsum dolor sit amet, consectetur adipiscing elit</h3>
      <div class="post-meta"><span class="cat">Category</span><span>Sub Category</span><span>By Author</span></div>
      <p>Lorem ipsum dolor sit amet, consectetur adipiscing elit. Ut sed orci vitae mattis tincidunt sagittis auctor feugiat et.</p>
      <div class="post-actions">
        <span class="action"><svg width="18" height="22" viewBox="0 0 18 22" fill="none" stroke="#8a8592" stroke-width="1.4"><path d="M1 1h16v20l-8-6-8 6z"/></svg>Save</span>
        <span class="action"><svg width="22" height="22" viewBox="0 0 22 22" fill="none" stroke="#8a8592" stroke-width="1.4"><circle cx="17" cy="4" r="3"/><circle cx="5" cy="11" r="3"/><circle cx="17" cy="18" r="3"/><path d="M8 9.5l6-4M8 12.5l6 4"/></svg>Share</span>
        <time>March 02, 2009</time>
      </div>
    </div>
  </article>
</section>

<div class="load-more abs">
  <svg width="20" height="12" viewBox="0 0 20 12" fill="none" stroke="#8a8592" stroke-width="1.6"><path d="M1 1l9 9 9-9"/></svg>
  <span>Load More Item</span>
</div>

<footer class="footer abs">
  <div class="footer-logo">Your Name<br>Here</div>
  <ul class="social">
    <li>Notes</li>
    <li>Friends</li>
    <li>Work</li>
  </ul>
  <p class="copyright">© 2022 Your Name</p>
</footer>

</body>
</html>
```